Create a professional, eye-catching business card design that reflects the values and services of Brookfern Veterinary Hospital. we provide veterinary services and the business card should be a memorable representation of the clinic and align with its branding and mission. our tag line is "Life Long Companions, Lifelong Care"
Use clean, modern typography. Prioritize readability and professionalism. We would like to see designs that use the color blue, as in the logo example. the final design should communicate professionalism and care, with attention to detail.

```html
<!DOCTYPE html>
<html lang="en">
<head>
<meta charset="utf-8">
<title>Brookfern Veterinary Hospital – Business Card</title>
<link rel="stylesheet" href="https://fonts.googleapis.com/css2?family=Londrina+Solid:wght@900&family=Montserrat:wght@700&family=Poppins:wght@400&family=Mr+Dafoe&display=swap">
<style>
  :root {
    --backdrop: #a9a9a9;
    --navy: #1b2a5c;
    --navy-deep: #142150;
    --white: #ffffff;
    --yellow: #ffd200;
    --cushion: #e8b92e;
    --ring: rgba(255,255,255,0.9);
  }
  * { margin: 0; padding: 0; box-sizing: border-box; }
  html, body { width: 1200px; height: 1155px; overflow: hidden; }
  body { background: var(--backdrop); position: relative; font-family: "Poppins", sans-serif; }

  .card {
    position: absolute;
    width: 521px;
    height: 910px;
    overflow: hidden;
    box-shadow: 0 10px 22px rgba(0,0,0,0.35);
  }
  .card--front { left: 50px; top: 117px; background: linear-gradient(180deg, #1e2e63 0%, var(--navy-deep) 100%); }
  .card--back { left: 624px; top: 119px; background: linear-gradient(180deg, #1e2e63 35%, var(--navy-deep) 100%); }

  .abs { position: absolute; }
  .center { left: 0; right: 0; text-align: center; }

  .brand-ring { border-radius: 50%; }
  .card--front .brand-ring { left: 198px; top: 118px; width: 130px; height: 130px; border: 2px solid var(--ring); }
  .brand-name {
    font-family: "Montserrat", sans-serif;
    font-weight: 700;
    line-height: 1;
  }
  .brand-name .main { display: block; font-size: 40px; letter-spacing: 0.5px; }
  .brand-name .sub { display: block; font-size: 15.5px; letter-spacing: 0.6px; margin-top: 4px; }
  .card--front .brand-name { top: 262px; color: var(--white); }

  .tagline {
    font-family: "Londrina Solid", sans-serif;
    font-weight: 900;
    color: var(--yellow);
    font-size: 64px;
    line-height: 58px;
    letter-spacing: 1px;
    top: 378px;
  }
  .tagline-accent { top: 386px; }
  .tagline-accent.left { left: 92px; }
  .tagline-accent.right { left: 376px; }

  .pet-photo {
    left: 36px; top: 673px; width: 453px; height: 237px;
    border-radius: 120px 120px 0 0;
    background: linear-gradient(180deg, #3a3f52 0%, #cfcfcf 45%, #e9e3d4 60%, var(--cushion) 75%, #d6a923 100%);
  }

  .back-top { left: 0; top: 0; width: 521px; height: 313px; background: var(--white); }
  .card--back .brand-ring { left: 182px; top: 75px; width: 156px; height: 120px; border: 2px solid var(--navy); border-bottom: none; border-radius: 78px 78px 0 0; }
  .card--back .brand-name { top: 202px; color: var(--navy); }

  .person-name {
    top: 348px;
    font-family: "Londrina Solid", sans-serif;
    font-weight: 900;
    color: var(--yellow);
    font-size: 58px;
    line-height: 58px;
    letter-spacing: 1px;
  }
  .person-role { top: 403px; color: var(--white); font-size: 24px; line-height: 30px; }
  .divider {
    left: 98px; top: 440px; width: 328px; height: 2px;
    background: linear-gradient(90deg, transparent, var(--yellow) 25%, var(--yellow) 60%, #2a2f48);
  }
  .icon-row { left: 90px; top: 479px; }

  .contact { color: var(--white); font-size: 20px; line-height: 26px; }
  .contact.phone { top: 549px; }
  .contact.address { top: 590px; }
  .contact.email { top: 660px; }
  .contact.web { top: 699px; }

  .follow {
    left: 115px; top: 758px;
    font-family: "Mr Dafoe", cursive;
    color: var(--white);
    font-size: 34px;
    line-height: 40px;
  }
  .social { top: 766px; width: 29px; height: 29px; border-radius: 5px; background: var(--yellow); }
  .social.one { left: 290px; }
  .social.two { left: 332px; }
  .social.three { left: 375px; }
</style>
</head>
<body>

<section class="card card--front">
  <div class="abs brand-ring"></div>
  <div class="abs center brand-name">
    <span class="main">BROOKFERN</span>
    <span class="sub">VETERINARY HOSPITAL</span>
  </div>

  <svg class="abs tagline-accent left" width="44" height="36" viewBox="0 0 44 36" aria-hidden="true">
    <g stroke="#ffd200" stroke-width="5" stroke-linecap="round" fill="none">
      <line x1="4" y1="18" x2="38" y2="18"/>
      <line x1="22" y1="4" x2="38" y2="16"/>
      <line x1="22" y1="32" x2="38" y2="20"/>
    </g>
  </svg>
  <svg class="abs tagline-accent right" width="44" height="36" viewBox="0 0 44 36" aria-hidden="true">
    <g stroke="#ffd200" stroke-width="5" stroke-linecap="round" fill="none">
      <line x1="6" y1="18" x2="40" y2="18"/>
      <line x1="6" y1="16" x2="22" y2="4"/>
      <line x1="6" y1="20" x2="22" y2="32"/>
    </g>
  </svg>
  <h1 class="abs center tagline">LIFELONG<br>COMPANIONS<br>LIFELONG CARE</h1>

  <div class="abs pet-photo" role="img" aria-label="Photo of a dark grey cat and a fluffy white dog resting together on a yellow cushion"></div>
</section>

<section class="card card--back">
  <div class="abs back-top"></div>
  <div class="abs brand-ring"></div>
  <div class="abs center brand-name">
    <span class="main">BROOKFERN</span>
    <span class="sub">VETERINARY HOSPITAL</span>
  </div>

  <h2 class="abs center person-name">MARCUS ELLERY</h2>
  <p class="abs center person-role">Veterinarian</p>
  <div class="abs divider"></div>

  <svg class="abs icon-row" width="345" height="36" viewBox="0 0 345 36" aria-hidden="true">
    <g stroke="#ffd200" stroke-width="1.5">
      <line x1="0" y1="12" x2="80" y2="12"/>
      <line x1="18" y1="18" x2="80" y2="18"/>
      <line x1="30" y1="24" x2="80" y2="24"/>
      <line x1="262" y1="12" x2="343" y2="12"/>
      <line x1="262" y1="18" x2="325" y2="18"/>
      <line x1="262" y1="24" x2="310" y2="24"/>
    </g>
    <g fill="#ffd200">
      <rect x="80" y="2" width="32" height="32" rx="8"/>
      <rect x="130" y="2" width="32" height="32" rx="8"/>
      <rect x="178" y="2" width="32" height="32" rx="8"/>
      <rect x="229" y="2" width="32" height="32" rx="8"/>
    </g>
    <g fill="none" stroke="#1b2a5c" stroke-width="2.2" stroke-linecap="round" stroke-linejoin="round">
      <path d="M89 11 q0 -2 2 -2 l3 0 l1.5 4 l-2 1.5 q2 4 6 6 l1.5 -2 l4 1.5 l0 3 q0 2 -2 2 q-14 -1 -14 -14z"/>
      <path d="M146 28 q-7 -8 -7 -13 a7 7 0 0 1 14 0 q0 5 -7 13z"/>
      <circle cx="146" cy="15" r="2.4"/>
      <rect x="186" y="11" width="16" height="12" rx="1.5"/>
      <path d="M186 12 l8 6 l8 -6"/>
      <circle cx="245" cy="18" r="8"/>
      <ellipse cx="245" cy="18" rx="3.5" ry="8"/>
      <line x1="237" y1="18" x2="253" y2="18"/>
    </g>
  </svg>

  <p class="abs center contact phone">(08) 9340 2268</p>
  <p class="abs center contact address">12 Ridgeview Lane,<br>Glenmore, WA 6109</p>
  <p class="abs center contact email">reception@brookfernvet.com.au</p>
  <p class="abs center contact web">www.brookfernvet.com.au</p>

  <p class="abs follow">Follow us on</p>
  <span class="abs social one"></span>
  <span class="abs social two"></span>
  <span class="abs social three"></span>
</section>

</body>
</html>
```